Help Lu Wenshao redesign his business card!

Lu Wenshao, an "influential" Chinese businessman, made international headlines this week with his business card...but not for the right reasons. Help Lu Wenshao redesign his new business card - funny and/or satirical submissions welcome!

Check out his hilarious business card that he was giving out on a trip to New York, with not one, not two...but TEN titles! Let's just say they're not the most humble titles either :).

Read more about Lu's business card here: http://notes.dailyledgerpost.example/asiadesk/2014/01/14/lu-wenshaos-business-card-needs-to-be-recycled/

While the rest of the world is laughing at him, we want to help. This is an unofficial contest, but we'd like the PixelGuild community to have a shot at redesigning Lu's business card. Thousands of businesses have used PixelGuild.example to create beautiful business cards, so we know the community of designers here can do a great job.

We'd like you to create a business card worthy of this honorable businessman, while also keeping a clean, dignified design.

Funny / satirical job titles and designs are encouraged. Note you do not have to use all of Lu's titles on the card. Feel free to come up with your own creative titles!

In regard to contact details, please use dummy contact details. Lu's company name and street address are:

China Meiling-Ta Reusable Scrap & Recovery Corporation
Baitang Road 7, Qiaoxin District, Nanjing, China

You can design a single sided or double-sided card - it's completely up to you!

We've put $200 up for grabs for the winning entry, which we will email to Lu in an effort to have him using a much more stylish card. Who knows, you might just have China's most important businessman using your design.

Target Market(s)

Business people and government officials of the world

Industry/Entity Type

Business

Font styles to use
Serif
Sans Serif
Decorative

Colors
ec2027
ffc214
6b449b
0455a3

Requirements
Must have
• At least 1 title, preferably more than 1.

Designers can approach this task how they like however one option could be to use one of Lu's titles and create a suitable business card graphic to suit the role. Designers are also encouraged to o make up a new title and design a graphic to suit.

Here are the titles - but you can also make up your own!

Most influential person of China
Most prominent Philanthropist of China
China Moral Leader
China Earthquake Rescue Hero
Most well-known and Beloved Chinese Role Model
China Top Ten Most Honorable Volunteer
Most Charismatic Philanthropist of China
China Low Carbon Emission
Environmental Protection Top Advocate
China's Foremost Environmental Preservation Demolition Expert
Should not have
• No black borders around photographs of Lu Wenshao
Do not present Lu Wenshao's image in grayscale (black and white)

For a detailed guideline for colors to avoid in design targeting the Chinese market, see http://www.quarrystoneadvisors.example/2011/01/17/color/

```html
<!DOCTYPE html>
<html lang="en">
<head>
<meta charset="utf-8">
<title>Lu Wenshao — Business Card</title>
<link rel="stylesheet" href="https://fonts.googleapis.com/css2?family=Alegreya+Sans:wght@400&display=swap">
<style>
  :root {
    --teal: #10b7cd;
    --sky-band: #55cfe0;
    --leaf: #4cd900;
    --lime: #80ff00;
    --white: #ffffff;
  }
  html, body {
    margin: 0;
    padding: 0;
    width: 1200px;
    height: 702px;
    overflow: hidden;
    background: var(--teal);
  }
  .card {
    position: relative;
    width: 1200px;
    height: 702px;
    overflow: hidden;
    font-family: "Alegreya Sans", "Trebuchet MS", sans-serif;
  }
  .card-bands {
    position: absolute;
    inset: 0;
    display: block;
  }
  .band-top-leaf { fill: var(--leaf); }
  .band-light { fill: var(--sky-band); }
  .band-main { fill: var(--teal); }
  .band-lime { fill: var(--lime); }
  .emblem-circle {
    position: absolute;
    left: 513px;
    top: 193px;
    width: 170px;
    height: 170px;
    border-radius: 50%;
    background: var(--white);
  }
  .holder-name {
    position: absolute;
    left: 0;
    right: 0;
    top: 372px;
    margin: 0;
    text-align: center;
    color: var(--white);
    font-weight: 400;
    font-size: 66px;
    line-height: 1;
    letter-spacing: 0.5px;
  }
  .holder-title {
    position: absolute;
    left: 0;
    right: 0;
    top: 494px;
    margin: 0;
    text-align: center;
    color: var(--white);
    font-weight: 400;
    font-size: 41px;
    line-height: 1;
  }
</style>
</head>
<body>
  <main class="card">
    <svg class="card-bands" width="1200" height="702" viewBox="0 0 1200 702" aria-hidden="true">
      <rect class="band-top-leaf" x="0" y="0" width="1200" height="79"/>
      <rect class="band-light" x="0" y="79" width="1200" height="56"/>
      <path class="band-lime" d="M427 0 H1200 V111 H522 A95 95 0 0 1 427 16 Z"/>
      <rect class="band-main" x="0" y="135" width="1200" height="442"/>
      <rect class="band-light" x="0" y="577" width="1200" height="56"/>
      <rect class="band-top-leaf" x="0" y="633" width="1200" height="69"/>
      <path class="band-lime" d="M0 601 H672 A100 100 0 0 1 772 701 V702 H0 Z"/>
    </svg>
    <div class="emblem-circle"></div>
    <h1 class="holder-name">Lu Wenshao</h1>
    <p class="holder-title">enviromental protection advocate</p>
  </main>
</body>
</html>
```